The Verdant Ledger App - Modernization & Graphics User Interface Friendliness Updates

We are Verdant Ledger, and we want to bring a new branding look and graphical user interface to the Verdant Ledger App. The app is a quick reference encyclopedia for all things produce. Boasting articles on over 2,000 produce items, with information ranging from taste and application to geographical and cultural significance. Included in its features are over 10 thousand recipes, and the Verdant Ledger App Harvest Circle – a global initiative to connect farmer, customer, and chef in one sustainable and easy to use application. The design needs to bring a greater sense of social connection – encouraging the user to participate in the 'Harvest Circled' experience voluntarily. The design should reflect a sense of authority reflecting the authenticity and reliability of the provided information, it's writing, and its sources. Download the App here: vledgr.example/install

Target Market(s)

Women and Men between ages 21-55.

Industry/Entity Type

Education

Font styles to use
Serif
Sans Serif

Colors

Designer to choose colors to be used in the design.

Requirements
Must have
• An updated user interface, the intuitive usability of the app is currently non-existent. We are looking to reflect as the authority on produce. The app design must reflect a professional, user-friendly, up-to-date, and trustworthy feel.
Nice to have
• To incorporate the social draw of the Harvest Circle we would like to include on the home page "Social Bubbles" (think Pictoloop stories) which updates with shared photos of produce and their location.
Should not have
• An overly complicated theme, distracting or unprofessional colors, and images.

```html
<!DOCTYPE html>
<html lang="en">
<head>
<meta charset="utf-8">
<title>Verdant Ledger — Home</title>
<link href="https://fonts.googleapis.com/css2?family=Roboto:wght@400;500&display=swap" rel="stylesheet">
<style>
  :root{
    --stage:#ececec;
    --screen:#f4f5f4;
    --brand:#4fbd4f;
    --brand-dark:#46ad46;
    --brand-line:#5fc95f;
    --card:#ffffff;
    --ink:#2b2b2b;
    --muted:#a9a9a9;
    --divider:#e3e3e3;
  }
  *{box-sizing:border-box;margin:0;padding:0}
  html,body{width:1200px;height:675px;overflow:hidden}
  body{background:var(--stage);font-family:"Roboto",Arial,sans-serif;color:var(--ink);display:flex;justify-content:center}
  .app-screen{position:relative;width:380px;height:675px;background:var(--screen);overflow:hidden;box-shadow:0 10px 40px rgba(0,0,0,.08)}
  .app-header{position:relative;height:190px;background:var(--brand);padding:22px 18px 0}
  .header-texture{position:absolute;inset:0;background:linear-gradient(180deg,var(--brand) 0%,var(--brand-dark) 100%);opacity:.6}
  .top-bar{position:relative;display:flex;align-items:center;justify-content:space-between;height:34px}
  .menu-icon,.profile-icon{width:30px;height:30px}
  .app-title{color:#fff;font-size:21px;font-weight:500;letter-spacing:.2px}
  .search-bar{position:relative;margin-top:24px;height:44px;background:#fff;border-radius:3px;display:flex;align-items:center;padding:0 12px;box-shadow:0 2px 6px rgba(0,0,0,.08)}
  .search-bar svg{width:18px;height:18px;flex:none}
  .search-placeholder{flex:1;margin-left:10px;color:#c4c4c4;font-size:14px}
  .filter-select{display:flex;align-items:center;gap:10px;padding-left:16px;border-left:1px solid var(--divider);height:24px;color:var(--brand);font-size:14px}
  .quick-links{position:absolute;left:12px;right:12px;top:140px;display:flex;background:var(--card);border-radius:4px;box-shadow:0 2px 8px rgba(0,0,0,.06);height:96px}
  .quick-link{flex:1;display:flex;flex-direction:column;align-items:center;justify-content:center;gap:8px;font-size:13px;text-align:center;line-height:1.2}
  .quick-link + .quick-link{border-left:1px solid var(--divider)}
  .quick-link svg,.quick-link .icon-fill{width:32px;height:32px}
  .icon-fill{border-radius:50%;background:linear-gradient(160deg,#bfe6bf,#8fd18f)}
  .section{padding:0 12px}
  .section-title{font-size:17px;font-weight:400;margin:0 0 10px 4px}
  .content{padding-top:62px}
  .product-row{display:flex;gap:10px;margin-bottom:20px;width:440px}
  .product-card{flex:none;width:96px;height:104px;background:var(--card);border-radius:4px;display:flex;flex-direction:column;align-items:center;padding-top:12px;box-shadow:0 1px 4px rgba(0,0,0,.05)}
  .product-photo{width:66px;height:46px;border-radius:10px}
  .product-name{margin-top:8px;font-size:11px;text-align:center;line-height:1.25;padding:0 4px}
  .ph-red{background:linear-gradient(135deg,#d4343a,#8e1c22)}
  .ph-orange{background:linear-gradient(135deg,#f4b63a,#d98a1e)}
  .ph-ginger{background:linear-gradient(135deg,#e3c590,#b9914f)}
  .ph-purple{background:linear-gradient(135deg,#5a3c8e,#2f1f4f)}
  .ph-yellow{background:linear-gradient(135deg,#f3d24a,#c9a12a)}
  .ph-green{background:linear-gradient(135deg,#c3dc7a,#88b548)}
  .ph-artichoke{background:linear-gradient(135deg,#7a9a4a,#4d6a2c)}
  .ph-violet{background:linear-gradient(135deg,#8d4d9a,#caa9c8)}
  .fab{position:absolute;right:18px;top:440px;width:54px;height:54px;border-radius:50%;background:var(--brand);display:flex;align-items:center;justify-content:center;box-shadow:0 4px 12px rgba(79,189,79,.4)}
  .fab svg{width:20px;height:20px}
</style>
</head>
<body>
<main class="app-screen">
  <header class="app-header">
    <div class="header-texture" role="img" aria-label="Faint storefront line pattern across the header"></div>
    <div class="top-bar">
      <svg class="menu-icon" viewBox="0 0 30 30"><g stroke="#fff" stroke-width="2.4" stroke-linecap="round"><line x1="4" y1="8" x2="24" y2="8"/><line x1="4" y1="15" x2="24" y2="15"/><line x1="4" y1="22" x2="24" y2="22"/></g></svg>
      <h1 class="app-title">Verdant Ledger</h1>
      <svg class="profile-icon" viewBox="0 0 30 30"><circle cx="15" cy="15" r="13" fill="none" stroke="#fff" stroke-width="2"/><circle cx="15" cy="12" r="4.5" fill="#fff"/><path d="M7 24c2-5 14-5 16 0" fill="#fff"/></svg>
    </div>
    <div class="search-bar">
      <svg viewBox="0 0 18 18"><circle cx="7.5" cy="7.5" r="5.5" fill="none" stroke="#bbb" stroke-width="1.8"/><line x1="11.5" y1="11.5" x2="16" y2="16" stroke="#bbb" stroke-width="1.8" stroke-linecap="round"/></svg>
      <span class="search-placeholder">Search Produce</span>
      <span class="filter-select">All
        <svg width="12" height="8" viewBox="0 0 12 8"><path d="M1 1l5 5 5-5" fill="none" stroke="#999" stroke-width="1.5"/></svg>
      </span>
    </div>
  </header>

  <nav class="quick-links">
    <div class="quick-link">
      <svg viewBox="0 0 32 32"><path d="M6 6h11l10 10-11 11L6 17z" fill="none" stroke="var(--brand)" stroke-width="1.8" stroke-linejoin="round"/><circle cx="11" cy="11" r="2" fill="var(--brand)"/></svg>
      <span>Offers</span>
    </div>
    <div class="quick-link">
      <div class="icon-fill" role="img" aria-label="Farmer line icon"></div>
      <span>Farmers<br>Market</span>
    </div>
    <div class="quick-link">
      <svg viewBox="0 0 32 32"><g fill="none" stroke="var(--brand)" stroke-width="1.8" stroke-linejoin="round"><line x1="16" y1="4" x2="16" y2="29"/><path d="M5 8h18l4 3-4 3H5z"/><path d="M27 17H9l-4 3 4 3h18z"/></g></svg>
      <span>Virtual Tour</span>
    </div>
  </nav>

  <div class="content">
    <section class="section">
      <h2 class="section-title">All Products</h2>
      <div class="product-row">
        <article class="product-card"><div class="product-photo ph-red" role="img" aria-label="Red acerola cherries"></div><p class="product-name">Acerola</p></article>
        <article class="product-card"><div class="product-photo ph-orange" role="img" aria-label="Orange acerola fruit"></div><p class="product-name">Acerola</p></article>
        <article class="product-card"><div class="product-photo ph-ginger" role="img" aria-label="Fresh ginger root"></div><p class="product-name">Adarak</p></article>
        <article class="product-card"><div class="product-photo ph-purple" role="img" aria-label="Purple akebi fruit"></div><p class="product-name">Akebi Fruit Purple</p></article>
      </div>
    </section>
    <section class="section">
      <h2 class="section-title">Available in Stock</h2>
      <div class="product-row">
        <article class="product-card"><div class="product-photo ph-yellow" role="img" aria-label="Yellow crabapples on a branch"></div><p class="product-name">European Crabapples</p></article>
        <article class="product-card"><div class="product-photo ph-green" role="img" aria-label="Golden delicious apples"></div><p class="product-name">Golden Delicious Appl.</p></article>
        <article class="product-card"><div class="product-photo ph-artichoke" role="img" aria-label="Thorny artichokes"></div><p class="product-name">Artichokes With Thorns</p></article>
        <article class="product-card"><div class="product-photo ph-violet" role="img" aria-label="Purple striped peppers"></div><p class="product-name">Purple Peppers</p></article>
      </div>
    </section>
    <section class="section">
      <h2 class="section-title">Spring Special</h2>
    </section>
  </div>

  <button class="fab" aria-label="Write">
    <svg viewBox="0 0 20 20"><path d="M13 2l5 5-9 9H4v-5z" fill="#fff"/><path d="M4 18h12" stroke="#fff" stroke-width="1.6"/></svg>
  </button>
</main>
</body>
</html>
```